Flyer-Design für Werbeflyer Teamentwicklung/Coaching als pdf
Zielgruppe
ich berate Personen, Teams und Organisationseinheiten, überwiegend im Profitbereich. (Internationale Konzerne). Mein Beratungsspektrum ist Führung, Prozessverbesserungen, Teamentwicklung
Aufgabenstellung
Der Text ist in Anlehnung an meine HP, Teamentwicklung und Coaching und es sollte eine übersichtliche, infomative 1-2 Seiten entstehen, die ich als erste Werbung/Kontaktaufnahme versenden kann. Die Seiten sollen klar einen Überblick über mein "Schaffen" geben, sollen aber auch schon etwas von meiner Arbeitsweise deutlich machen. (Ich begriefe schnell, formuliere klar und arbeite sehr zielorientiert - allerdings auch schnörkellos!) Diese Seiten sollten überwiegend als Anhang an eine Mail fungieren, im Ausnahmefall aber auch versendet werden.
Das Logo, die Farbe, etc. analog zu meiner HP - ich lass mich da aber auch gern beraten, falls sie andere Ideen haben

```html
<!DOCTYPE html>
<html lang="de">
<head>
<meta charset="utf-8">
<title>Teamentwicklung Mirela Tebbe – Flyer</title>
<link href="https://fonts.googleapis.com/css2?family=Open+Sans:wght@400;600&display=swap" rel="stylesheet">
<style>
  :root {
    --sage: #b9c9c4;
    --sage-dark: #9eaeaa;
    --plum: #780a56;
    --heading: #6b7573;
    --text: #5f6866;
    --white: #ffffff;
  }
  * { margin: 0; padding: 0; box-sizing: border-box; }
  html, body { width: 1200px; height: 848px; overflow: hidden; background: var(--white); }
  body { font-family: "Open Sans", Arial, sans-serif; color: var(--text); position: relative; }
  .flyer { position: relative; width: 1200px; height: 848px; overflow: hidden; background: var(--white); }

  .hero-photo {
    position: absolute; left: 0; top: 100px; width: 337px; height: 748px;
    background: linear-gradient(180deg, #5f93c9 0%, #bcd3ea 18%, #e9eef2 30%, #a9b4bd 40%, #7d7e7c 46%, #8e8a84 60%, #6f6b66 80%, #5a5651 100%);
  }

  .header-band {
    position: absolute; left: 0; top: 19px; width: 1200px; height: 81px; background: var(--sage);
  }
  .brand-square {
    position: absolute; left: 30px; top: 19px; width: 86px; height: 81px; background: var(--sage-dark);
  }
  .brand-title {
    position: absolute; left: 146px; top: 27px; color: var(--white); font-weight: 600; line-height: 1;
  }
  .brand-title .line-1 { display: block; font-size: 31px; letter-spacing: 0.3px; }
  .brand-title .line-2 { display: block; font-size: 25px; margin-top: 7px; letter-spacing: 0.3px; }

  .contact-box {
    position: absolute; left: 956px; top: 0; width: 216px; height: 181px; background: var(--plum);
    color: var(--white); font-size: 15px; line-height: 18px; padding: 21px 0 0 16px;
  }
  .contact-box p + p { margin-top: 18px; }

  .section-heading {
    position: absolute; color: var(--heading); font-weight: 600; font-size: 26px; letter-spacing: 0.4px; line-height: 1;
  }
  .body-text { position: absolute; font-size: 13px; line-height: 15.6px; hyphens: auto; }
  .body-text p + p { margin-top: 15.6px; }

  .sub-heading {
    position: absolute; left: 384px; top: 317px; font-size: 13.7px; font-weight: 600; color: var(--heading); letter-spacing: 0.3px;
  }

  .bullet-list { position: absolute; list-style: none; font-size: 13px; line-height: 15.6px; hyphens: auto; }
  .bullet-list li { position: relative; padding-left: 19px; margin-bottom: 7px; }
  .bullet-list li::before {
    content: ""; position: absolute; left: 0; top: 4px; width: 8px; height: 8px; background: var(--plum);
  }
  .bullet-list.tight li { margin-bottom: 5.5px; }
</style>
</head>
<body>
<div class="flyer">

  <div class="hero-photo" role="img" aria-label="Foto: hölzerner Steg mit Geländer, der unter blauem Wolkenhimmel aufs Meer hinausführt"></div>

  <div class="header-band"></div>
  <div class="brand-square"></div>
  <div class="brand-title">
    <span class="line-1">TEAMENTWICKLUNG</span>
    <span class="line-2">MIRELA TEBBE</span>
  </div>

  <div class="contact-box">
    <p>Lindenhof<br>Ahornweg 14-16<br>90478 Fürth</p>
    <p>Tel:&nbsp; 0911 - 58 21 47<br>Fax: 0911 - 5 82 19 60<br>info@mirela-tebbe.de<br>www.mirela-tebbe.de</p>
  </div>

  <h2 class="section-heading" style="left:380px; top:192px;">TEAMENTWICKLUNG</h2>
  <div class="body-text" style="left:380px; top:229px; width:466px;">
    <p>Teams sind lebendige Gebilde, die um erfolgreich zu sein, sich immer wieder neu ausrichten und koordinieren müssen. Das tun sie in aller Regel ohne fremde Hilfe - aber ab und zu ist es hilfreich, Impulse oder Entwicklungsförderung von außen bekommen.</p>
  </div>

  <h3 class="sub-heading">DAZU GEHÖREN</h3>
  <ul class="bullet-list" style="left:380px; top:347px; width:218px;">
    <li>Eine sorgfältige Analyse der Situation und Festlegung gewünschter Resultate</li>
    <li>Überzeugende und förderliche Methoden, die die Lösungskompetenzen der Menschen im Team unterstützen.</li>
  </ul>
  <ul class="bullet-list" style="left:620px; top:347px; width:210px;">
    <li>Klare Führung durch den Widerstreit von Teaminteressen zwischen Verändern, Bewahren, Harmonie und Konfliktbearbeitung, klarem Feedback und Eintracht im Team</li>
    <li>Tragfähigkeit der Ergebnisse</li>
  </ul>

  <h2 class="section-heading" style="left:918px; top:248px;">SEMINARE</h2>
  <div class="body-text" style="left:918px; top:288px; width:240px;">
    <p>In auf spezielle Themen ausgerichteten Seminaren finde ich mit Ihnen Strategien, um wiederkehrende Situationen positiv für Sie oder Ihr Unternehmen zu nutzen.</p>
  </div>

  <h2 class="section-heading" style="left:918px; top:390px;">ANGEBOT</h2>
  <div class="body-text" style="left:918px; top:431px; width:240px;">
    <p>Erfolgreiches Fehlermanagement durch konstruktive Kommunikation</p>
  </div>

  <h2 class="section-heading" style="left:380px; top:512px;">COACHING</h2>
  <div class="body-text" style="left:380px; top:550px; width:240px;">
    <p>Business-Coaching ist die professionelle Beratung und Begleitung, um Ihre beruflichen Ziele zu erreichen.</p>
    <p>Diese Form der Beratung wendet sich an Führungskräfte und andere Potentialträger in Organisationen und an Selbstständige.</p>
    <p>Coaching wirkt am besten, wenn berufliche Fragen nur eine einzelne Person betreffen, die sich konzentriert, zielgerichtet und zügig selbst verändern will.</p>
    <p>Schon wenige Termine, manchmal auch nur eine intensive Sitzung, reichen aus,</p>
  </div>
  <div class="body-text" style="left:646px; top:550px; width:236px;">
    <p>um eine Entwicklung auszulösen. Das Lernen geschieht bewusst und ganz konkret am jeweiligen Thema.</p>
    <p>Erfolgreiches Coaching lebt von gegenseitigem Vertrauen und Respekt.</p>
    <p>Ich verstehen meine Aufgabe darin, Ihnen durch geeignete Methoden und intelligente Gesprächsführung neue Perspektiven zu eröffnen – kurz, Sie dabei zu unterstützen, sich weiterzuentwickeln, Ihre Leistungsfähigkeit zu steigern und nach Ihren Maßstäben erfolgreich zu arbeiten.</p>
  </div>
  <ul class="bullet-list tight" style="left:928px; top:550px; width:240px;">
    <li>für eine festgelegte Zeit durch einen beruflichen Sparringspartner eine andere Sichtweise kennen zu lernen, so dass neue Perspektiven entstehen</li>
    <li>Stärkung der Führungsqualitäten</li>
    <li style="margin-bottom:0;">Führungsstil und Führungsrolle</li>
    <li>Mitarbeiterführung</li>
    <li>Kooperationsstrategien</li>
    <li>Stärkenprofil, persönliches Potenzial</li>
    <li>einen latenten oder akuten Konflikt dauerhaft lösen zu wollen</li>
    <li>Karriereplanung</li>
    <li>Burn-out-Prophylaxe</li>
  </ul>

</div>
</body>
</html>
```